Bramble Fitness Flyer

Need a flyer to showcase my fitness facility with a focus on "PERSONAL TRAINING". To be used in paper advertisements.

I've added some photos below. Please make sure to use our logo as well as the pictures below (use as many as you like).

Also please make sure to add our contact info:

4-18 236th st.
Whitestone NY, 11357

718-555-0417

contact@bramblefit-example.com

Lastly please make sure to add a "Contact us for a free trial!" stamp somewhere on the page.

```html
<!DOCTYPE html>
<html lang="en">
<head>
<meta charset="utf-8">
<title>Bramble Fitness – Personal Training Flyer</title>
<link rel="stylesheet" href="https://fonts.googleapis.com/css2?family=Exo+2:ital,wght@0,700;0,800;1,800;1,900&family=Roboto:wght@400;700&display=swap">
<style>
  :root {
    --page: #d6d6d8;
    --charcoal: #262626;
    --charcoal-soft: #333333;
    --lime: #8dc63f;
    --white: #ffffff;
    --mist: #c9c9cc;
    --band: rgba(120, 120, 124, 0.55);
    --text-dark: #1e1e1e;
  }
  * { margin: 0; padding: 0; box-sizing: border-box; }
  html, body {
    width: 1176px; height: 1200px; overflow: hidden;
    background: var(--page);
  }
  .flyer {
    position: absolute; left: 158px; top: 43px;
    width: 860px; height: 1113px; overflow: hidden;
    background: linear-gradient(180deg, var(--mist) 0%, #e4e4e6 55%, var(--white) 75%);
    font-family: "Roboto", sans-serif;
  }
  .hero-photo {
    position: absolute; left: 310px; top: 60px; width: 550px; height: 660px;
    background: linear-gradient(135deg, #6b4a38 0%, #b08c74 40%, #7a6b86 65%, #e8e4e2 100%);
  }
  .hero-fade {
    position: absolute; left: 0; top: 560px; width: 860px; height: 260px;
    background: linear-gradient(180deg, rgba(255,255,255,0) 0%, rgba(250,248,248,0.9) 60%, #faf7f6 100%);
  }
  .texture {
    position: absolute; left: 0; top: 700px; width: 860px; height: 413px;
    background: linear-gradient(160deg, #f4f2f2 0%, #ffffff 50%, #f6efec 100%);
  }
  .header { position: absolute; left: 0; top: 0; }
  .brand {
    position: absolute; left: 52px; top: 44px;
    display: flex; align-items: center; gap: 16px;
  }
  .brand-dot { width: 56px; height: 56px; border-radius: 50%; background: var(--lime); }
  .brand-name {
    font-family: "Exo 2", sans-serif; font-weight: 800;
    color: var(--white); font-size: 44px; line-height: 0.95; letter-spacing: 2px;
    text-transform: uppercase;
  }
  .snapshot {
    position: absolute; background: var(--white); padding: 7px;
    box-shadow: 0 4px 12px rgba(0,0,0,0.25);
  }
  .snapshot div { width: 100%; height: 100%; }
  .snapshot--outdoor { left: 51px; top: 255px; width: 237px; height: 245px; transform: rotate(-4deg); }
  .snapshot--outdoor div { background: linear-gradient(180deg, #7fa4d6 0%, #d9d2c8 55%, #9a9590 100%); }
  .snapshot--gym { left: 81px; top: 492px; width: 210px; height: 247px; transform: rotate(3deg); }
  .snapshot--gym div { background: linear-gradient(180deg, #e6eef2 0%, #b9c3c8 50%, #4a4d52 100%); }
  .headline { position: absolute; left: 0; top: 0; }
  .headline-word {
    position: absolute; font-family: "Exo 2", sans-serif; font-style: italic; font-weight: 900;
    text-transform: uppercase; line-height: 1; white-space: nowrap; text-align: center;
  }
  .headline-word--personal { left: 226px; top: 656px; width: 496px; font-size: 86px; color: var(--charcoal); }
  .headline-word--training { left: 94px; top: 772px; width: 610px; font-size: 98px; color: var(--white); letter-spacing: 1px; }
  .contact-band {
    position: absolute; left: 0; top: 954px; width: 860px; height: 108px;
    background: var(--band);
  }
  .contact {
    position: absolute; left: 81px; top: 988px; color: var(--text-dark);
    font-size: 23px; line-height: 1.3; font-style: normal;
  }
  .contact strong { font-weight: 700; }
  .contact .divider { margin: 0 8px; }
  .trial-tag { position: absolute; left: 602px; top: 940px; width: 156px; height: 146px; }
  .trial-text {
    position: absolute; left: 602px; top: 968px; width: 156px; text-align: center;
    color: var(--white); font-size: 17px; line-height: 1.25; text-transform: uppercase;
  }
  .trial-text b { color: var(--lime); font-weight: 700; }
</style>
</head>
<body>
  <main class="flyer">
    <div class="hero-photo" role="img" aria-label="Photo of women training with suspension straps in the gym"></div>
    <div class="hero-fade"></div>
    <div class="texture" role="img" aria-label="Faint geometric background texture"></div>

    <svg class="header" width="860" height="260" viewBox="0 0 860 260" aria-hidden="true">
      <polygon points="0,0 860,0 860,102 0,212" fill="var(--charcoal)"/>
      <polygon points="0,212 860,102 860,120 0,230" fill="var(--lime)"/>
    </svg>

    <div class="brand">
      <span class="brand-dot"></span>
      <span class="brand-name">Bramble<br>Fitness</span>
    </div>

    <figure class="snapshot snapshot--outdoor"><div role="img" aria-label="Photo of a man training outside the gym entrance"></div></figure>
    <figure class="snapshot snapshot--gym"><div role="img" aria-label="Photo of the gym floor with cardio machines"></div></figure>

    <svg class="headline" width="860" height="920" viewBox="0 0 860 920" aria-hidden="true">
      <polygon points="238,648 730,648 716,750 224,750" fill="var(--lime)"/>
      <polygon points="742,735 770,735 752,800 724,800" fill="var(--lime)"/>
      <polygon points="104,750 712,750 694,895 84,895" fill="var(--charcoal)"/>
      <polygon points="58,830 96,830 86,868 48,868" fill="var(--lime)"/>
    </svg>
    <h1>
      <span class="headline-word headline-word--personal">Personal</span>
      <span class="headline-word headline-word--training">Training</span>
    </h1>

    <div class="contact-band"></div>
    <address class="contact">
      4-18 236th st. Whitestone NY, 11357<br>
      <strong>718-555-0417</strong><span class="divider">|</span>contact@bramblefit-example.com
    </address>

    <svg class="trial-tag" viewBox="0 0 156 146" aria-hidden="true">
      <polygon points="0,0 156,0 156,146 78,116 0,146" fill="var(--charcoal-soft)"/>
    </svg>
    <p class="trial-text">Contact us<br>for a<br><b>Free trial!</b></p>
  </main>
</body>
</html>
```